Premium CBD/Hemp company needs packaging and label design

Verdant Oakfield, a premium CBD/Hemp company based in Scottsdale, Arizona is in need of a packaging and label design. We are launching with our flagship product which will be a 30 count capsule and will come in three functions: Pain Relief, Anxiety Support, and Sleep Support. For the purpose of this contest, please design packaging and label for our Anxiety Support product. Our products are physician formulated and all natural. Our main ingredient is CBD/Hemp and is complemented by specific herbs that synergistically work together to give the customer the most effective and desired result. We would like our branding to have a pharmaceutical look and feel with a focus on trust and transparency. We have uploaded our company logo that is to be used on both the packaging and label. We have also uploaded an executed branding questionnaire that will guide you to exactly what we are seeking to achieve as to the look and feel of our brand. Please feel free to contact us with any questions that you may have. The winner of this contest will have the opportunity to work with us on future projects as we will need packaging and label design for our entire Verdant Oakfield product line.

Target Market(s)

See attached branding questionnaire

Industry/Entity Type

Health And Wellness

Font styles to use
Sans Serif

Colors

Designer to choose colors to be used in the design.

Requirements
Must have
• See attached branding questionnaire; Please superimpose labels onto a cobalt blue capsule bottle (see attached)
• >>UPON REVIEW of the FIRST 8 designs, we really like the silver, mildly metallic label background in DESIGN # 21300528, we do not want metalic lettering as that would not look very "Pharmaceutical"
• >>We are in search of a look that is a bit more "Pharmaceutical" than a look that would be more commonly found in a Supplement Store
Nice to have
• "See attached branding questionnaire
Should not have
• See attached branding questionnaire; NO marijuana or cannabis plant on the packaging or label

```html
<!DOCTYPE html>
<html lang="en">
<head>
<meta charset="utf-8">
<title>Verdant Oakfield – Anxiety Support Packaging</title>
<link href="https://fonts.googleapis.com/css2?family=Open+Sans:wght@400;600;700&display=swap" rel="stylesheet">
<style>
  :root {
    --cobalt: #253f92;
    --cobalt-soft: #3a55a6;
    --leaf-green: #1f9a4a;
    --silver: #c9cbd0;
    --silver-dark: #9a9da3;
    --white: #ffffff;
    --ink-grey: #555a63;
    --page: #ffffff;
  }
  * { box-sizing: border-box; margin: 0; padding: 0; }
  html, body { width: 1200px; height: 1200px; overflow: hidden; background: var(--page); }
  body { position: relative; font-family: "Open Sans", sans-serif; }

  .panel { position: absolute; background: var(--cobalt); }
  .box-top { left: 172px; top: 129px; width: 402px; height: 317px; }
  .box-top .frame {
    position: absolute; inset: 20px 18px 24px 18px;
    border: 2px solid var(--silver);
  }
  .box-top .brand {
    position: absolute; left: 0; right: 0; top: 142px;
    display: flex; align-items: center; justify-content: center; gap: 14px;
  }
  .brand-dot { border-radius: 50%; flex: none; }
  .box-top .brand-dot { width: 44px; height: 44px; border: 2px solid var(--silver); }
  .box-top .brand-name { color: var(--silver); font-size: 30px; font-weight: 400; }

  .box-front { left: 172px; top: 463px; width: 402px; height: 646px; }
  .leaf-pattern {
    position: absolute; inset: 0;
    background: radial-gradient(circle at 30% 20%, #3550a0 0%, var(--cobalt) 60%);
  }

  .label { position: absolute; background: var(--white); border: 1px solid var(--silver); overflow: hidden; }
  .box-front .label { left: 45px; top: 59px; width: 312px; height: 531px; }

  .label .brand { position: absolute; left: 0; right: 0; display: flex; align-items: center; justify-content: center; }
  .label .brand-dot { background: var(--leaf-green); }
  .label .brand-name { color: var(--cobalt); font-weight: 400; }

  .title { position: absolute; left: 0; right: 0; text-align: center; }
  .title-main { display: block; color: var(--leaf-green); font-weight: 700; }
  .title-sub { display: block; color: var(--cobalt); font-weight: 400; }
  .rule {
    position: absolute; height: 3px;
    background: linear-gradient(90deg, var(--silver-dark), #eceef0 40%, var(--silver-dark));
  }
  .tagline { position: absolute; left: 0; right: 0; text-align: center; color: var(--ink-grey); }
  .count { position: absolute; color: var(--cobalt); letter-spacing: .1em; }
  .badge {
    position: absolute; border-radius: 50%; background: var(--leaf-green); color: var(--white);
    display: flex; align-items: center; justify-content: center; text-align: center; line-height: 1.3;
    letter-spacing: .08em;
  }
  .hand-art { position: absolute; background: linear-gradient(160deg, var(--cobalt-soft), var(--cobalt)); border-radius: 70% 20% 0 80%; }

  /* large front label */
  .box-front .brand { top: 60px; gap: 12px; }
  .box-front .brand-dot { width: 36px; height: 36px; }
  .box-front .brand-name { font-size: 24px; }
  .box-front .title { top: 170px; }
  .box-front .title-main { font-size: 48px; letter-spacing: .05em; line-height: 1.05; }
  .box-front .title-sub { font-size: 36px; letter-spacing: .32em; line-height: 1.1; }
  .box-front .rule { left: 42px; width: 230px; top: 268px; }
  .box-front .tagline { top: 292px; font-size: 13px; }
  .box-front .count { left: 48px; top: 482px; font-size: 14px; }
  .box-front .badge { left: 170px; top: 395px; width: 76px; height: 76px; font-size: 11px; z-index: 2; }
  .box-front .hand-art { left: 150px; top: 440px; width: 140px; height: 91px; }

  /* bottle label, version one */
  .bottle-label-a { left: 802px; top: 294px; width: 134px; height: 185px; }
  .bottle-label-a .brand { top: 24px; gap: 5px; }
  .bottle-label-a .brand-dot { width: 14px; height: 14px; }
  .bottle-label-a .brand-name { font-size: 10px; }
  .bottle-label-a .title { top: 62px; }
  .bottle-label-a .title-main { font-size: 20px; letter-spacing: .04em; line-height: 1.05; }
  .bottle-label-a .title-sub { font-size: 15px; letter-spacing: .28em; line-height: 1.1; }
  .bottle-label-a .rule { left: 18px; width: 98px; top: 102px; height: 2px; }
  .bottle-label-a .tagline { top: 110px; font-size: 6px; }
  .bottle-label-a .count { left: 32px; top: 164px; font-size: 5px; }
  .bottle-label-a .badge { left: 76px; top: 137px; width: 28px; height: 28px; font-size: 4px; z-index: 2; }
  .bottle-label-a .hand-art { left: 68px; top: 154px; width: 56px; height: 31px; }

  /* bottle label, version two */
  .bottle-label-b { left: 775px; top: 834px; width: 156px; height: 203px; }
  .bottle-label-b .brand { top: 24px; gap: 5px; }
  .bottle-label-b .brand-dot { width: 16px; height: 16px; }
  .bottle-label-b .brand-name { font-size: 11px; }
  .bottle-label-b .title { top: 70px; }
  .bottle-label-b .title-main { font-size: 22px; letter-spacing: .04em; line-height: 1.05; }
  .bottle-label-b .title-sub { font-size: 16px; letter-spacing: .28em; line-height: 1.1; }
  .bottle-label-b .rule { left: 25px; width: 106px; top: 113px; height: 2px; }
  .bottle-label-b .tagline { top: 121px; font-size: 6.5px; }
  .leaf-strip {
    position: absolute; left: 0; right: 0; bottom: 0; height: 58px;
    background: linear-gradient(0deg, var(--cobalt-soft), rgba(58,85,166,.35));
  }
</style>
</head>
<body>

  <section class="panel box-top">
    <div class="frame"></div>
    <div class="brand">
      <span class="brand-dot"></span>
      <span class="brand-name">Verdant Oakfield</span>
    </div>
  </section>

  <section class="panel box-front">
    <div class="leaf-pattern" role="img" aria-label="Faint scattered leaf pattern on cobalt blue"></div>
    <div class="label">
      <div class="brand">
        <span class="brand-dot"></span>
        <span class="brand-name">Verdant Oakfield</span>
      </div>
      <h1 class="title"><span class="title-main">ANXIETY</span><span class="title-sub">SUPPORT</span></h1>
      <div class="rule"></div>
      <p class="tagline">Lorem ipsum Lorem ipsum</p>
      <p class="count">30 TABLETS</p>
      <div class="badge">PURE<br>HEMP</div>
      <div class="hand-art" role="img" aria-label="Cobalt illustration of a hand and branch rising from the corner"></div>
    </div>
  </section>

  <section class="label bottle-label-a">
    <div class="brand">
      <span class="brand-dot"></span>
      <span class="brand-name">Verdant Oakfield</span>
    </div>
    <h2 class="title"><span class="title-main">ANXIETY</span><span class="title-sub">SUPPORT</span></h2>
    <div class="rule"></div>
    <p class="tagline">Lorem ipsum Lorem ipsum</p>
    <p class="count">30 TABLETS</p>
    <div class="badge">PURE<br>HEMP</div>
    <div class="hand-art" role="img" aria-label="Cobalt illustration of a hand and branch"></div>
  </section>

  <section class="label bottle-label-b">
    <div class="brand">
      <span class="brand-dot"></span>
      <span class="brand-name">Verdant Oakfield</span>
    </div>
    <h2 class="title"><span class="title-main">ANXIETY</span><span class="title-sub">SUPPORT</span></h2>
    <div class="rule"></div>
    <p class="tagline">Lorem ipsum Lorem ipsum</p>
    <div class="leaf-strip" role="img" aria-label="Cobalt falling leaves and hand illustration along the label base"></div>
  </section>

</body>
</html>
```